Plakat-Design: Hausmesse Robotik und Cobots
Zielgruppe
High-Tech Engineering aus Euskirchen
Die KW Technikwerk & Servicepartner GmbH mit Sitz in Euskirchen entwickelt moderne Maschinen Robotiklösungen für Kunden in der Region, überregional und bundesweit. Mittelständische Unternehmen und Maschinenbauer, internationale Großkonzerne aus der Konsumgüterindustrie und Hersteller von Maschinen für die weiterverarbeitende Industrie vertrauen KW seit vielen Jahren.
> Maschinenbau
> Automation
> Robotik
> Certified Systemintegrator für Falkmann Greifsysteme
Aufgabenstellung
Projektauftrag:
Flyer/Plakat zur Einladung Hausmesse
Format:
> Din A4 PDF zur Einladung der Kunten (digital)
> Werbebanner für E-Mail Signatur
Daten der Messe:
> 18.05.2022 10-17 Uhr
> KW Technik , Lerchenfeldweg 14, 53879 Euskirchen
> Anmeldeplattform folgt
Motto der Veranstaltung:
> 'Automation - so einfach'
> 'Einfach automatisieren mit Cobots'
> Für Vorschläge gerne offen
Was erwartet Sie:
> Roboter Demos
> Kamerageführte Robotik
> Plug & Play Lösungen
Ausstellerinformationen:
> Bitte unten Platz für Logos der Aussteller vorsehen (derzeit ca. 15)
> Logos können später übermittelt werden
Infomaterial für den Designer:
>> www.kw-technikwerk.de
>> www.falkmann-greif.de
>> Weitere Bilder sind vorhanden.
>> Farbeschema der PowerPoint nutzen (Vertriebspräsentation_de_KW_21-06-23.pptx)

```html
<!DOCTYPE html>
<html lang="de">
<head>
<meta charset="utf-8">
<title>Automation – so einfach · Hausmesse KW Technik</title>
<link rel="stylesheet" href="https://fonts.googleapis.com/css2?family=Josefin+Sans:wght@300;400;600;700&display=swap">
<style>
  :root {
    --navy-deep: #141f5a;
    --navy: #1c2d78;
    --navy-bright: #2c55b8;
    --panel-blue: #0f2d5e;
    --panel-blue-2: #12346b;
    --white: #ffffff;
    --silver-light: #e4e8ee;
    --silver: #aab3c0;
    --silver-dark: #59626f;
    --graphite: #1a1d24;
    --text-dark: #1b2a55;
    --slot-grey: #e3e7ee;
    --divider: #1c3d74;
  }
  * { box-sizing: border-box; margin: 0; padding: 0; }
  html, body { width: 848px; height: 1200px; overflow: hidden; background: var(--white); }
  body { font-family: "Josefin Sans", sans-serif; }

  .poster { position: relative; width: 848px; height: 1200px; overflow: hidden; }

  .hero {
    position: absolute; left: 0; top: 0; width: 848px; height: 952px;
    background:
      radial-gradient(ellipse 60% 45% at 55% 30%, rgba(70,120,220,0.55) 0%, rgba(70,120,220,0) 100%),
      linear-gradient(180deg, var(--navy) 0%, var(--navy-deep) 100%);
  }
  .robot-photo {
    position: absolute; left: 182px; top: 50px; width: 560px; height: 520px;
    border-radius: 28px;
    background:
      radial-gradient(ellipse 35% 30% at 72% 62%, rgba(26,29,36,0.85) 0%, rgba(26,29,36,0) 100%),
      linear-gradient(135deg, var(--silver-light) 0%, var(--silver) 40%, var(--silver-dark) 75%, var(--graphite) 100%);
    box-shadow: 0 20px 50px rgba(5,10,40,0.45);
  }

  .title-box {
    position: absolute; left: 40px; top: 571px; width: 752px; height: 138px;
    background: var(--panel-blue);
    display: flex; align-items: center; justify-content: center;
    box-shadow: 0 8px 24px rgba(0,0,0,0.25);
  }
  .title {
    color: var(--white); font-weight: 400; font-size: 96px; letter-spacing: 0;
    line-height: 1; padding-top: 12px;
  }
  .subtitle-box {
    position: absolute; left: 239px; top: 717px; width: 374px; height: 74px;
    background: var(--panel-blue-2);
    display: flex; align-items: center; justify-content: center;
  }
  .subtitle {
    color: var(--white); font-weight: 600; font-size: 30px; letter-spacing: 7px;
    padding-top: 6px;
  }

  .event-date { position: absolute; left: 74px; top: 842px; color: var(--white); }
  .event-date .day { font-weight: 700; font-size: 26px; letter-spacing: 6px; }
  .event-date .hours { font-weight: 300; font-size: 26px; letter-spacing: 9px; margin-top: 8px; }

  .highlights {
    position: absolute; left: 428px; top: 832px; list-style: none; color: var(--white);
    font-size: 21px; font-weight: 400; line-height: 29px;
  }
  .highlights li::before { content: "•"; margin-right: 12px; }

  .info-panel {
    position: absolute; left: 0; top: 952px; width: 848px; height: 205px; background: var(--white);
  }
  .brand { position: absolute; left: 40px; top: 44px; display: flex; align-items: center; gap: 10px; }
  .brand-mark { width: 22px; height: 22px; background: var(--panel-blue); }
  .brand-name { font-weight: 700; font-size: 32px; color: var(--panel-blue); padding-top: 6px; }
  .address {
    position: absolute; left: 40px; top: 136px; color: var(--text-dark);
    font-size: 18px; line-height: 24px; font-style: normal;
  }
  .divider {
    position: absolute; left: 303px; top: 36px; width: 2px; height: 142px; background: var(--divider);
  }
  .exhibitors {
    position: absolute; left: 348px; top: 45px; width: 444px;
    display: grid; grid-template-columns: repeat(7, 1fr); gap: 6px;
  }
  .exhibitor-slot { height: 58px; background: var(--slot-grey); }

  .footer {
    position: absolute; left: 0; top: 1157px; width: 848px; height: 43px; background: var(--panel-blue);
    display: flex; align-items: center; justify-content: center;
    color: var(--white); font-size: 19px; letter-spacing: 1px; padding-top: 4px;
  }
</style>
</head>
<body>
<main class="poster">
  <section class="hero" role="img" aria-label="Dunkelblauer Hintergrund mit leuchtendem Leiterbahn-Muster">
    <div class="robot-photo" role="img" aria-label="Foto eines silbernen Cobot-Roboterarms mit Kamera und Greifer"></div>
  </section>

  <div class="title-box"><h1 class="title">AUTOMATION</h1></div>
  <div class="subtitle-box"><p class="subtitle">- SO EINFACH</p></div>

  <div class="event-date">
    <p class="day">18.MAI 2022</p>
    <p class="hours">10-17 UHR</p>
  </div>

  <ul class="highlights">
    <li>Roboter Demos</li>
    <li>Kamerageführte Robotik</li>
    <li>Plug &amp; Play Lösungen</li>
  </ul>

  <section class="info-panel">
    <div class="brand">
      <span class="brand-mark"></span>
      <span class="brand-name">KW Technik</span>
    </div>
    <address class="address">
      Lerchenfeldweg 14<br>53879 Euskirchen
    </address>
    <span class="divider"></span>
    <div class="exhibitors" aria-label="Platz für Aussteller-Logos">
      <span class="exhibitor-slot"></span><span class="exhibitor-slot"></span><span class="exhibitor-slot"></span><span class="exhibitor-slot"></span><span class="exhibitor-slot"></span><span class="exhibitor-slot"></span><span class="exhibitor-slot"></span>
      <span class="exhibitor-slot"></span><span class="exhibitor-slot"></span><span class="exhibitor-slot"></span><span class="exhibitor-slot"></span><span class="exhibitor-slot"></span><span class="exhibitor-slot"></span><span class="exhibitor-slot"></span>
    </div>
  </section>

  <footer class="footer">www.kw-technikwerk.de</footer>
</main>
</body>
</html>
```